4Star Hotel looking for web design

Hello everyone,
We are located in Cambodia, the hotel should open in 2-3 months. The name will be Velmora-Boutique Hotel. We are looking for a webdesign which is professional, elegant and SIMPLE.
All informations should be easy to find. We are quite open to proposition but we would like to the home page:
-a carousel with around 5-8 picture
-Little menu where we can book a room
By the way, we would like a page for our restaurant, gallery, contact page for description of the rooms. I add some old pictures.
I give an example of what we are expecting:
www.quenrostays.com/tovelspring
We hope that we are proposing a good job for you guys. Have fun and Thanks.
Oh and the winner ( or someone he had choose) of course have free night in our presidential suite
Target Market(s)
We are looking for european Market. Let s say people middle age who are willing to travel in difficult area
Industry/Entity Type
Hotel
Coding
Coded - Design and coding required
Number of Pages Required
5+ page
Requirements
Must have
- Simple, simple and Simple
- Carousel
- place for book a room
- during booking, a menu for select room , and after that another menu for propose like tour in town, taxi, flower, bottle of champagne for example
- during all the process, the customer should be able to know at what step it is and can stop and come back after
- Have to be perfect for smartphone
- Price with drawbar for they know how much they earn with our reduction
Nice to have
- during the process of information (name, adress, tel...), it would be great if they can fill it with a button facebook, google plus, lindkdin, instagram ....
- then a button share on facebook, twitter for know that they book in our hotel
- At the end of the booking, a flashcode with the recapitulatif that customer can scan.

```html
<!DOCTYPE html>
<html lang="en">
<head>
<meta charset="utf-8">
<title>Velmora-Boutique Hotel</title>
<link href="https://fonts.googleapis.com/css2?family=Open+Sans:wght@400;600;700;800&display=swap" rel="stylesheet">
<style>
:root{
  --maroon-deep:#3a0606;
  --maroon:#4e0b0b;
  --red:#8c1c12;
  --red-bright:#a92c1a;
  --red-soft:#b5442e;
  --ink:#2b2b2b;
  --muted:#777;
  --line:#d8d8d8;
  --paper:#ffffff;
  --gray-bg:#ececec;
  --white:#fff;
}
*{box-sizing:border-box;margin:0;padding:0}
html,body{width:1200px;height:2440px;overflow:hidden}
body{font-family:"Open Sans",Arial,sans-serif;color:var(--ink);background:var(--paper);position:relative}

/* header */
.site-header{position:absolute;top:0;left:0;width:1200px;height:100px;background:var(--paper);z-index:5}
.brand{position:absolute;left:60px;top:22px;display:flex;align-items:center;gap:12px}
.brand-mark{width:40px;height:40px;background:var(--red)}
.brand-name{font-size:22px;font-weight:700;color:var(--red)}
.top-bar{position:absolute;right:60px;top:10px;display:flex;gap:20px;align-items:center;font-size:11px;color:var(--muted)}
.top-bar .social{display:flex;gap:5px}
.top-bar .social span{width:16px;height:16px;background:var(--red-soft);display:block}
.main-nav{position:absolute;right:60px;top:58px;display:flex;gap:30px;font-size:16px;font-weight:600}
.main-nav a{color:var(--ink);text-decoration:none}
.main-nav a.active{color:var(--red)}
.dropdown{position:absolute;left:548px;top:94px;width:120px;background:var(--red);z-index:6;padding:4px 0}
.dropdown li{list-style:none;font-size:11px;color:var(--white);padding:5px 10px;border-bottom:1px solid rgba(255,255,255,.15)}
.dropdown li.current{background:var(--white);color:var(--red);margin:0 4px}

/* hero */
.hero{position:absolute;top:0;left:0;width:1200px;height:540px;background:linear-gradient(180deg,#dcdcdc 0%,#a9a9a9 45%,#6f6f6f 70%,#3f3f3f 100%)}
.hero-arrow{position:absolute;top:300px;width:48px;height:56px;background:rgba(0,0,0,.45);display:flex;align-items:center;justify-content:center}
.hero-arrow.prev{left:30px}.hero-arrow.next{right:30px}
.hero-caption{position:absolute;left:56px;top:446px;color:var(--white)}
.hero-caption h1{font-size:24px;font-weight:700;letter-spacing:.5px}
.hero-caption p{margin-top:6px;font-size:13px;background:var(--red);padding:3px 8px;display:inline-block}
.hero-book{position:absolute;right:56px;top:480px;text-align:center;color:var(--white)}
.hero-book strong{display:block;font-size:18px;font-weight:800}
.hero-book small{font-size:9px;opacity:.85}

/* availability */
.availability-band{position:absolute;top:540px;left:0;width:1200px;height:120px;background:var(--maroon);display:flex;align-items:center;justify-content:center}
.availability-band h2{color:var(--white);font-size:40px;font-weight:700;letter-spacing:1px}
.booking-form{position:absolute;top:660px;left:0;width:1200px;height:160px;background:var(--paper)}
.field{position:absolute;top:40px}
.field label{display:block;font-size:14px;color:var(--muted);margin-bottom:10px}
.field .box{height:38px;border:1px solid var(--line);font-size:13px;color:var(--muted);display:flex;align-items:center;justify-content:space-between;padding:0 10px}
.btn-check{position:absolute;left:972px;top:80px;width:170px;height:38px;background:var(--red);color:var(--white);font-size:13px;font-weight:600;display:flex;align-items:center;justify-content:center}
.divider{position:absolute;top:820px;left:0;width:1200px;height:20px;background:var(--gray-bg)}

/* features */
.features{position:absolute;top:840px;left:0;width:1200px;height:760px;background:linear-gradient(180deg,#5a100c 0%,#7a1a12 50%,#5a100c 100%);color:var(--white);text-align:center}
.features h2{margin-top:90px;font-size:44px;font-weight:800}
.features .lead{margin:20px auto 0;width:820px;font-size:15px;opacity:.85}
.feature{position:absolute;top:230px;width:300px;text-align:center}
.feature .icon{width:128px;height:128px;border-radius:50%;margin:0 auto;display:flex;align-items:center;justify-content:center}
.feature .icon.red{background:var(--red-bright)}
.feature .icon.white{background:var(--white)}
.feature h3{margin-top:24px;font-size:17px;font-weight:600}
.feature p{margin:14px auto 0;width:230px;font-size:12px;line-height:1.6;opacity:.85}
.btn-more{display:inline-block;margin-top:40px;padding:10px 28px;font-size:13px;background:var(--red-bright);color:var(--white)}
.btn-more.light{background:var(--white);color:var(--red)}

/* news cards */
.news{position:absolute;top:1600px;left:0;width:1200px;height:700px;background:var(--gray-bg)}
.card{position:absolute;top:190px;height:470px}
.card.side{width:240px;background:var(--red)}
.card .photo{height:230px;background:linear-gradient(160deg,#c98a5a,#6a3a22)}
.card.side .body{padding:22px 20px;color:var(--white);text-align:center}
.card.side h4{font-size:13px;font-weight:700;line-height:1.4}
.card.side p{margin-top:14px;font-size:11px;line-height:1.6;opacity:.9}
.meta{position:absolute;bottom:12px;left:16px;right:16px;display:flex;justify-content:space-between;font-size:10px;color:var(--white);opacity:.9}
.card.feature-post{left:330px;width:540px;background:linear-gradient(180deg,#5b5b5b,#1e1e1e);color:var(--white);text-align:center}
.card.feature-post .meta{top:16px;bottom:auto;left:24px;right:24px}
.card.feature-post h4{margin:150px auto 0;width:420px;font-size:20px;font-weight:400;line-height:1.45}
.card.feature-post p{margin:18px auto 0;width:380px;font-size:11px;line-height:1.6;opacity:.8}
.btn-outline{display:inline-block;margin-top:26px;padding:9px 22px;border:1px solid var(--white);font-size:11px;letter-spacing:1px}

/* footer */
.site-footer{position:absolute;top:2300px;left:0;width:1200px;height:140px;background:var(--maroon-deep);color:var(--white);text-align:center}
.footer-nav{margin-top:24px;display:flex;justify-content:center;gap:22px;font-size:12px;font-weight:600}
.footer-social{margin-top:16px;display:flex;justify-content:center;gap:10px}
.footer-social span{width:26px;height:26px;background:var(--red-soft);display:block}
.copyright{margin-top:22px;font-size:11px;opacity:.8}
</style>
</head>
<body>

<section class="hero" role="img" aria-label="Carousel photo of a wide river landscape under a pale sky"></section>
<div class="hero-arrow prev"><svg width="16" height="22" viewBox="0 0 16 22"><path d="M12 2 3 11l9 9" stroke="#fff" stroke-width="3" fill="none"/></svg></div>
<div class="hero-arrow next"><svg width="16" height="22" viewBox="0 0 16 22"><path d="M4 2l9 9-9 9" stroke="#fff" stroke-width="3" fill="none"/></svg></div>
<div class="hero-caption">
  <h1>WELCOME TO VELMORA</h1>
  <p>Lorem Ipsum is simply dummy text of the printing and typesetting</p>
</div>
<div class="hero-book"><strong>BOOK NOW</strong><small>BEST RATES ASSURED</small></div>

<header class="site-header">
  <div class="brand"><span class="brand-mark"></span><span class="brand-name">Velmora</span></div>
  <div class="top-bar">
    <span>Languages</span><span>Create Account</span><span>Follow us</span>
    <div class="social"><span></span><span></span><span></span></div>
  </div>
  <nav class="main-nav">
    <a href="#">Home</a>
    <a href="#" class="active">Accommodation</a>
    <a href="#">Restaurant &amp; Bar</a>
    <a href="#">Meeting and events</a>
    <a href="#">Blog</a>
    <a href="#">Special packages</a>
  </nav>
</header>
<ul class="dropdown">
  <li>Suite</li>
  <li class="current">Junior Suite</li>
  <li>Family room</li>
  <li>Cambodia Room</li>
  <li>Deluxe room</li>
  <li>Standard room</li>
</ul>

<section class="availability-band"><h2>CHECK AVAILABILITY</h2></section>
<section class="booking-form">
  <div class="field" style="left:60px;width:160px"><label>Check in</label><div class="box">09-07-2022</div></div>
  <div class="field" style="left:320px;width:80px"><label>Night</label><div class="box">2 <span>▾</span></div></div>
  <div class="field" style="left:448px;width:160px"><label>Check out</label><div class="box">09-07-2022</div></div>
  <div class="field" style="left:712px;width:80px"><label>Adults</label><div class="box">2 <span>▾</span></div></div>
  <div class="field" style="left:840px;width:80px"><label>Children</label><div class="box">0</div></div>
  <div class="btn-check">CHECK AVAILABILITY</div>
</section>
<div class="divider"></div>

<section class="features" aria-label="Hotel highlights over an interior staircase photo">
  <h2>WE LOVE VELMORA HOTEL</h2>
  <p class="lead">Lorem Ipsum is simply dummy text of the printing and typesetting industry. Lorem Ipsum has been the</p>

  <div class="feature" style="left:50px">
    <div class="icon red"><svg width="56" height="56" viewBox="0 0 56 56" fill="#fff"><path d="M16 8h24v14a12 12 0 0 1-24 0z"/><path d="M16 12H8v4a8 8 0 0 0 8 8M40 12h8v4a8 8 0 0 1-8 8" stroke="#fff" stroke-width="3" fill="none"/><rect x="25" y="33" width="6" height="9"/><rect x="18" y="42" width="20" height="6"/></svg></div>
    <h3>LUXURY ACCOMMODATIONS</h3>
    <p>Quiet rooms with river views, soft linens and calm corners made for long, restful evenings after travel.</p>
    <span class="btn-more">Read More</span>
  </div>

  <div class="feature" style="left:450px">
    <div class="icon white"><svg width="60" height="56" viewBox="0 0 60 56" fill="none" stroke="#8c1c12" stroke-width="4"><rect x="6" y="8" width="48" height="32"/><path d="M22 50h16M30 40v10"/></svg></div>
    <h3>ONLINE RESERVATION</h3>
    <p>Pick your dates, choose a room and add extras in a few clear steps, then return whenever you like.</p>
    <span class="btn-more light">Read More</span>
  </div>

  <div class="feature" style="left:850px">
    <div class="icon red"><svg width="56" height="56" viewBox="0 0 56 56" fill="none" stroke="#fff" stroke-width="4"><rect x="8" y="20" width="40" height="10"/><rect x="12" y="30" width="32" height="18"/><path d="M28 20v28M28 20c-4-10-14-10-12-2 1 3 8 2 12 2 4 0 11 1 12-2 2-8-8-8-12 2"/></svg></div>
    <h3>SPECIAL OFFER</h3>
    <p>Seasonal packages with town tours, airport taxi and a chilled bottle waiting in your room on arrival.</p>
    <span class="btn-more">Read More</span>
  </div>
</section>

<section class="news">
  <article class="card side" style="left:60px">
    <div class="photo" role="img" aria-label="Photo of a hotel corridor with warm wooden doors"></div>
    <div class="body">
      <h4>LOREM IPSUM IS SIMPLE DUMMY TEXT</h4>
      <p>Short stories from our garden, kitchen and rooms.</p>
    </div>
    <div class="meta"><span>Leon</span><span>27 May</span><span>1287</span></div>
  </article>

  <article class="card feature-post" role="img" aria-label="Dark photo of a hotel lobby behind the featured post">
    <div class="meta"><span>Leon</span><span>27 May</span><span>1287</span></div>
    <h4>Lorem Ipsum is simply dummy text of the typesetting industry. Lorem Ipsum has been the</h4>
    <p>Morning walks along the river, local markets and quiet temples wait just minutes from our front door each day.</p>
    <span class="btn-outline">READ MORE</span>
  </article>

  <article class="card side" style="left:900px">
    <div class="photo" role="img" aria-label="Photo of a decorated hotel room with carved wooden panels"></div>
    <div class="body">
      <h4>LOREM IPSUM IS SIMPLE DUMMY TEXT</h4>
      <p>News on menus, events and seasonal stays here.</p>
    </div>
    <div class="meta"><span>Leon</span><span>27 May</span><span>1287</span></div>
  </article>
</section>

<footer class="site-footer">
  <nav class="footer-nav">
    <span>HOME</span><span>ACCOMMODATION</span><span>RESTAURANT &amp; BAR</span><span>MEETING AND EVENTS</span><span>BLOG</span><span>SPECIAL PACKAGES</span>
  </nav>
  <div class="footer-social"><span></span><span></span><span></span><span></span><span></span></div>
  <p class="copyright">© 2015 ALL RIGHTS RESERVED</p>
</footer>

</body>
</html>
```